Book Cover Design Project

A non-fiction book on child protection, specifically... keeping young children safe from predators and keeping teenagers safe from themselves.

Title:
Under Our Roof

Subtitle:
A Guide To Keeping Your Children Safe

Author:
Martin Kellerby

```html
<!DOCTYPE html>
<html lang="en">
<head>
<meta charset="utf-8">
<title>Under Our Roof – Book Cover</title>
<link rel="stylesheet" href="https://fonts.googleapis.com/css2?family=Indie+Flower&family=Montserrat:wght@700&display=swap">
<style>
  :root {
    --ink: #000000;
    --paper: #ffffff;
    --key-grey: #6b6b6b;
    --key-grey-dark: #4e4e4e;
    --echo-light: #9a9a9a;
    --echo-dark: #262626;
    --echo-faint: #2e2e2e;
    --skin-light: #d9a07e;
    --skin-mid: #9c6448;
    --photo-light: #e8d3c6;
    --photo-mid: #9a7258;
  }
  html, body { margin: 0; padding: 0; overflow: hidden; background: var(--ink); }
  .cover {
    position: relative;
    width: 783px;
    height: 1200px;
    background: var(--ink);
    overflow: hidden;
  }
  .cover-art { position: absolute; inset: 0; display: block; }
  .title {
    font-family: "Indie Flower", cursive;
    font-size: 92px;
    fill: var(--paper);
  }
  .title-echo {
    font-family: "Indie Flower", cursive;
    fill: url(#echoFade);
    stroke: url(#echoFade);
    stroke-width: 2.5px;
  }
  .title-echo.faint {
    fill: var(--echo-faint);
    stroke: var(--echo-faint);
    stroke-width: 1.5px;
  }
  .subtitle {
    font-family: "Montserrat", sans-serif;
    font-weight: 700;
    font-size: 29px;
    fill: var(--paper);
  }
  .author {
    font-family: "Indie Flower", cursive;
    font-size: 38px;
    fill: var(--paper);
  }
</style>
</head>
<body>
<div class="cover">
  <svg class="cover-art" width="783" height="1200" viewBox="0 0 783 1200" xmlns="http://www.w3.org/2000/svg">
    <defs>
      <radialGradient id="eyesGlow" cx="0.5" cy="0.45" r="0.55">
        <stop offset="0" stop-color="var(--skin-light)"/>
        <stop offset="0.55" stop-color="var(--skin-mid)"/>
        <stop offset="1" stop-color="var(--ink)"/>
      </radialGradient>
      <radialGradient id="childTone" cx="0.5" cy="0.5" r="0.5">
        <stop offset="0" stop-color="var(--photo-light)"/>
        <stop offset="1" stop-color="var(--photo-mid)"/>
      </radialGradient>
      <linearGradient id="echoFade" x1="0" y1="0" x2="0" y2="1">
        <stop offset="0" stop-color="var(--echo-light)"/>
        <stop offset="1" stop-color="var(--echo-dark)"/>
      </linearGradient>
      <path id="subtitleArc" d="M 170 880 A 245 245 0 0 1 660 880"/>
    </defs>

    <ellipse class="eyes-photo" role="img" aria-label="Close-up photo of a woman's watchful eyes" cx="399" cy="150" rx="325" ry="160" fill="url(#eyesGlow)"/>

    <text class="title" x="392" y="425" text-anchor="middle">Under Our Roof</text>
    <text class="title-echo" transform="translate(415 528) scale(1 1.35)" x="0" y="0" text-anchor="middle" font-size="60" textLength="417" lengthAdjust="spacingAndGlyphs">Under Our Roof</text>
    <text class="title-echo faint" transform="translate(413 600) scale(1 1.3)" x="0" y="0" text-anchor="middle" font-size="30" textLength="208" lengthAdjust="spacingAndGlyphs">Under Our Roof</text>

    <text class="subtitle"><textPath href="#subtitleArc" startOffset="50%" text-anchor="middle" textLength="740" lengthAdjust="spacing">A Guide To Keeping Your Children Safe</textPath></text>

    <g class="keyhole">
      <circle cx="430" cy="820" r="150" fill="var(--key-grey)"/>
      <polygon points="439,962 482,940 482,1175 439,1175" fill="var(--key-grey-dark)"/>
      <rect x="338" y="962" width="101" height="213" fill="var(--paper)"/>
      <circle class="child-photo" role="img" aria-label="Photo of a thoughtful young girl with curly hair" cx="392" cy="826" r="147" fill="url(#childTone)"/>
    </g>

    <text class="author" x="568" y="1125">Author:</text>
    <text class="author" x="750" y="1162" text-anchor="end">Martin Kellerby</text>
  </svg>
</div>
</body>
</html>
```